Harborline Reserve Electric Company needs vehicle wraps

Need unique design for company vehicle wraps. We sell & install standby generators for homes and businesses. We provide our services in a high risk area for severe hurricanes, coastal flooding and power outages due to aging power grids.

Target Market(s)

Homes and businesses

Industry/Entity Type

Homes Services, Contractors

Requirements
Must have
• Graphics, extreme weather, flooding, power lines and storms depicted

```html
<!DOCTYPE html>
<html lang="en">
<head>
<meta charset="utf-8">
<title>Harborline Reserve Electric – Vehicle Wrap Sides</title>
<link rel="stylesheet" href="https://fonts.googleapis.com/css2?family=Poppins:ital,wght@0,400;0,700;0,800;1,700;1,800&display=swap">
<style>
  :root {
    --wrap-orange: #ef5a24;
    --wrap-gray: #6d6e71;
    --wrap-white: #ffffff;
    --page-bg: #f3f3f3;
    --panel-edge: #d9d9d9;
  }
  html, body {
    margin: 0;
    padding: 0;
    width: 1200px;
    height: 1200px;
    overflow: hidden;
    background: var(--page-bg);
  }
  .canvas {
    position: relative;
    width: 1200px;
    height: 1200px;
    font-family: "Poppins", sans-serif;
  }
  .wrap-side {
    position: absolute;
    left: 70px;
    width: 1060px;
    height: 380px;
  }
  .wrap-side--driver { top: 170px; }
  .wrap-side--passenger { top: 650px; }
  .panel-body { fill: var(--wrap-white); stroke: var(--panel-edge); stroke-width: 2; }
  .orange-field { fill: var(--wrap-orange); }
  .gray-arc { fill: none; stroke: var(--wrap-gray); stroke-width: 14; }
  .hazard-ring { fill: var(--wrap-orange); stroke: var(--wrap-white); stroke-width: 4; }
  .hazard-core { fill: var(--wrap-white); opacity: .35; }
  .hazard-label { fill: var(--wrap-orange); font-weight: 800; font-style: italic; font-size: 13px; }
  .brand-name { fill: var(--wrap-white); font-weight: 800; font-size: 50px; letter-spacing: -0.5px; }
  .brand-sub { fill: var(--wrap-white); font-weight: 800; font-size: 34px; letter-spacing: 1px; }
  .offer-head { fill: var(--wrap-white); font-weight: 800; font-size: 22px; }
  .offer-sub { fill: var(--wrap-white); font-weight: 700; font-style: italic; font-size: 17px; }
  .offer-note { fill: var(--wrap-white); font-weight: 400; font-size: 13px; }
  .phone { fill: var(--wrap-orange); font-weight: 800; font-style: italic; font-size: 24px; }
</style>
</head>
<body>
<main class="canvas">

  <!-- Driver side: graphics toward the rear (right) -->
  <svg class="wrap-side wrap-side--driver" viewBox="0 0 1060 380" aria-label="Wrap layout, driver side">
    <rect class="panel-body" x="1" y="1" width="1058" height="378" rx="40"/>
    <path class="orange-field" d="M640 1 Q570 200 680 379 L1019 379 Q1059 379 1059 339 L1059 41 Q1059 1 1019 1 Z"/>
    <path class="gray-arc" d="M612 1 Q540 200 650 379"/>

    <g class="hazard" role="img" aria-label="Extreme weather icon: tornado">
      <circle class="hazard-ring" cx="590" cy="60" r="26"/>
      <circle class="hazard-core" cx="590" cy="60" r="14"/>
    </g>
    <text class="hazard-label" x="555" y="55" text-anchor="end">Extreme</text>
    <text class="hazard-label" x="555" y="71" text-anchor="end">Weather</text>

    <g class="hazard" role="img" aria-label="Power lines icon: downed lines">
      <circle class="hazard-ring" cx="580" cy="130" r="26"/>
      <circle class="hazard-core" cx="580" cy="130" r="14"/>
    </g>
    <text class="hazard-label" x="545" y="135" text-anchor="end">Power Lines</text>

    <g class="hazard" role="img" aria-label="Flooding icon: house in water">
      <circle class="hazard-ring" cx="590" cy="202" r="26"/>
      <circle class="hazard-core" cx="590" cy="202" r="14"/>
    </g>
    <text class="hazard-label" x="555" y="207" text-anchor="end">Flooding</text>

    <text class="brand-name" x="680" y="95">HARBORLINE</text>
    <text class="brand-sub" x="722" y="140">RESERVE ELECTRIC</text>

    <text class="offer-head" x="655" y="228">SELL &amp; INSTALL</text>
    <text class="offer-sub" x="655" y="250">Standby Generators</text>
    <text class="offer-note" x="655" y="268">Homes and Businesses</text>

    <text class="phone" x="210" y="225">123-456-789</text>
  </svg>

  <!-- Passenger side: graphics toward the rear (left) -->
  <svg class="wrap-side wrap-side--passenger" viewBox="0 0 1060 380" aria-label="Wrap layout, passenger side">
    <rect class="panel-body" x="1" y="1" width="1058" height="378" rx="40"/>
    <path class="orange-field" d="M380 1 Q450 140 330 379 L41 379 Q1 379 1 339 L1 41 Q1 1 41 1 Z"/>
    <path class="gray-arc" d="M408 1 Q480 140 360 379"/>

    <g class="hazard" role="img" aria-label="Extreme weather icon: tornado">
      <circle class="hazard-ring" cx="440" cy="60" r="26"/>
      <circle class="hazard-core" cx="440" cy="60" r="14"/>
    </g>
    <text class="hazard-label" x="475" y="55">Extreme</text>
    <text class="hazard-label" x="475" y="71">Weather</text>

    <g class="hazard" role="img" aria-label="Power lines icon: downed lines">
      <circle class="hazard-ring" cx="445" cy="130" r="26"/>
      <circle class="hazard-core" cx="445" cy="130" r="14"/>
    </g>
    <text class="hazard-label" x="480" y="135">Power Lines</text>

    <g class="hazard" role="img" aria-label="Flooding icon: house in water">
      <circle class="hazard-ring" cx="430" cy="202" r="26"/>
      <circle class="hazard-core" cx="430" cy="202" r="14"/>
    </g>
    <text class="hazard-label" x="465" y="207">Flooding</text>

    <text class="brand-name" x="40" y="95">HARBORLINE</text>
    <text class="brand-sub" x="60" y="140">RESERVE ELECTRIC</text>

    <text class="offer-head" x="140" y="228">SELL &amp; INSTALL</text>
    <text class="offer-sub" x="140" y="250">Standby Generators</text>
    <text class="offer-note" x="140" y="268">Homes and Businesses</text>

    <text class="phone" x="625" y="225">123-456-789</text>
  </svg>

</main>
</body>
</html>
```